Land Development Company Website Redesign

We are looking for a fresh design for our website. The content will remain 90% the same.

We really like the layout style of www.quibbenstor.com.

We have attached our current site for content.

Industry/Entity Type

Real Estate Development

Coding

Coded - Design and coding required

Number of Pages Required

5+ page

Font styles to use
Sans Serif

Requirements
Must have
• Consistent feel across all the pages. Visually appealing and simple layout design that can be viewed on a mobile device and browser.

```html
<!DOCTYPE html>
<html lang="en">
<head>
<meta charset="utf-8">
<title>Cedar Ridge Estates</title>
<link href="https://fonts.googleapis.com/css2?family=Roboto+Condensed:wght@300;400&family=Open+Sans:wght@400;600&family=Dancing+Script:wght@700&display=swap" rel="stylesheet">
<style>
:root{
  --gold:#c9a063;
  --gold-btn:#d2aa6c;
  --dark:#333333;
  --darker:#2a2a2a;
  --text:#444;
  --muted:#888;
  --line:#d6d6d6;
  --white:#fff;
}
*{box-sizing:border-box;margin:0;padding:0}
html,body{width:1200px;height:4775px;overflow:hidden}
body{position:relative;background:var(--white);font-family:"Open Sans",Arial,sans-serif;color:var(--text)}
.abs{position:absolute}
.title{position:absolute;left:0;width:1200px;text-align:center;font-family:"Roboto Condensed",sans-serif;font-weight:400;font-size:40px;line-height:48px;letter-spacing:1px;color:var(--darker);text-transform:uppercase}
.title span{color:var(--gold)}
.title.light{color:var(--white)}
.script{position:absolute;left:0;width:1200px;text-align:center;font-family:"Dancing Script",cursive;font-size:22px;line-height:28px;color:var(--darker)}
.btn{position:absolute;background:var(--gold-btn);color:var(--darker);font-family:"Roboto Condensed",sans-serif;font-size:17px;text-align:center;text-transform:uppercase;letter-spacing:.5px}
.photo{position:absolute}

/* hero */
.hero{left:0;top:0;width:1200px;height:652px;background:
  radial-gradient(ellipse 280px 220px at 130px 520px,rgba(34,52,28,.95),rgba(34,52,28,0)),
  radial-gradient(ellipse 260px 260px at 1080px 470px,rgba(40,60,32,.95),rgba(40,60,32,0)),
  radial-gradient(ellipse 420px 230px at 470px 380px,rgba(206,186,150,.95),rgba(206,186,150,0)),
  radial-gradient(ellipse 200px 120px at 260px 440px,rgba(224,160,80,.8),rgba(224,160,80,0)),
  radial-gradient(ellipse 500px 110px at 600px 610px,rgba(88,110,58,.95),rgba(88,110,58,0)),
  linear-gradient(180deg,#a796b9 0%,#d4bccd 30%,#c6aeb6 45%,#7b7a62 68%,#445a34 86%,#33452a 100%)}
.brand{left:540px;top:30px;width:120px;height:130px;display:flex;align-items:center;justify-content:center;flex-direction:column;gap:6px}
.brand .mark{width:56px;height:56px;background:var(--darker)}
.brand .name{font-family:"Roboto Condensed",sans-serif;font-size:15px;color:var(--white);letter-spacing:1px;white-space:nowrap}
.nav{left:197px;top:200px;width:821px;height:55px;background:rgba(40,40,40,.82);display:flex;align-items:center;padding-left:10px}
.nav a{font-family:"Roboto Condensed",sans-serif;font-size:17px;color:var(--white);text-decoration:none;padding:0 18px;line-height:55px;text-transform:uppercase}
.nav a.active{background:rgba(255,255,255,.15);color:var(--gold)}

/* about */
.about-text{left:205px;top:834px;width:790px;font-size:13.5px;line-height:23px;text-align:center;color:var(--text)}

/* testimonial */
.testimonial{left:0;top:1050px;width:1200px;height:525px;background:
  radial-gradient(ellipse 700px 160px at 600px 1160px,rgba(190,200,210,.5),rgba(190,200,210,0)),
  linear-gradient(180deg,#303b46 0%,#5d6b78 22%,#8c97a0 38%,#5a6658 56%,#2f3b28 72%,#28301f 90%,#3a3a36 100%)}
.testimonial .bar{left:0;top:0;width:1200px;height:150px;background:rgba(20,30,40,.55)}
.quote{left:280px;top:1280px;width:640px;text-align:center;font-family:"Roboto Condensed",sans-serif;font-size:21px;line-height:32px;color:var(--white);text-transform:uppercase}
.author{left:0;top:1390px;width:1200px;text-align:center;font-size:16px;color:var(--white)}
.arrow{position:absolute;width:36px;height:36px;background:rgba(30,30,30,.7);display:flex;align-items:center;justify-content:center}
.arrow.grey{background:#555}

/* what's new */
.whatsnew{left:0;top:2126px;width:1200px;height:574px;background:
  radial-gradient(ellipse 300px 200px at 950px 300px,rgba(210,150,90,.6),rgba(210,150,90,0)),
  radial-gradient(ellipse 260px 300px at 120px 260px,rgba(60,36,20,.9),rgba(60,36,20,0)),
  linear-gradient(160deg,#5a3b22 0%,#8a6440 45%,#4a3220 100%)}
.whatsnew .shade{left:0;top:0;width:1200px;height:574px;background:rgba(40,30,20,.4)}
.new-text{left:535px;top:2262px;width:455px;font-size:13.5px;line-height:22px;color:var(--white)}
.hurry{left:0;top:2612px;width:1200px;text-align:center;font-family:"Roboto Condensed",sans-serif;font-size:19px;color:var(--white);text-transform:uppercase}
.hurry span{color:var(--gold)}

/* work */
.filters{left:0;top:2868px;width:1200px;display:flex;justify-content:center;gap:10px}
.filters span{border:1px solid #bbb;font-size:12px;padding:5px 14px;color:var(--text)}
.filters span.on{background:#666;color:var(--white);border-color:#666}

/* team */
.team{left:0;top:3358px;width:1200px;height:573px;background:
  radial-gradient(ellipse 300px 300px at 120px 280px,rgba(60,58,56,.9),rgba(60,58,56,0)),
  radial-gradient(ellipse 300px 260px at 1100px 320px,rgba(70,66,62,.9),rgba(70,66,62,0)),
  linear-gradient(120deg,#8b8680 0%,#d2ccc4 45%,#7f7a75 100%)}
.team .shade{left:0;top:0;width:1200px;height:573px;background:rgba(30,30,30,.3)}
.portrait{position:absolute;top:3533px;width:251px;height:255px}
.member{position:absolute;top:3800px;width:251px;text-align:center;color:var(--white)}
.member .n{font-family:"Roboto Condensed",sans-serif;font-size:22px;line-height:26px;text-transform:uppercase}
.member .r{font-size:12px;text-transform:uppercase;margin-top:6px}

/* form */
.field{position:absolute;border:1px solid var(--line);background:var(--white);font-size:13px;color:var(--muted);padding:13px 18px}
.field.focus{background:#eee;border-color:#bbb}

/* contact */
.contact-band{left:0;top:4440px;width:1200px;height:96px;background:var(--dark)}
.socials{left:0;top:4562px;width:1200px;display:flex;justify-content:center;gap:14px}
.socials i{width:38px;height:38px;display:block;background:#5a5a5a}
.contact-lines{left:0;top:4624px;width:1200px;text-align:center;font-size:13px;line-height:20px;color:var(--text)}
.contact-lines a{color:var(--gold);text-decoration:none}
.mini-mark{left:584px;top:4692px;width:32px;height:32px;background:var(--darker)}
.bottom-bar{left:0;top:4727px;width:1200px;height:48px;background:var(--darker);color:var(--white);font-size:13px;text-align:center;line-height:48px}
.bottom-bar span{color:var(--gold)}
</style>
</head>
<body>

<!-- hero -->
<div class="abs hero" role="img" aria-label="Photograph of a large stone estate house at dusk with landscaped lawn and fire pit"></div>
<div class="abs brand"><div class="mark"></div><div class="name">CEDAR RIDGE</div></div>
<nav class="abs nav">
  <a class="active">Home</a><a>What's New</a><a>The Estates</a><a>The Team</a><a>Gallery</a><a>Contact</a>
</nav>

<!-- about -->
<h2 class="title" style="top:705px">About <span>Cedar Ridge Estates</span></h2>
<p class="script" style="top:764px">Lorem ipsum is a dummy text</p>
<p class="abs about-text">Lorem Ipsum is simply dummy text of the printing and typesetting industry. Lorem Ipsum has been the industry's standard dummy text ever since the 1500s, when an unknown printer took a galley of type and scrambled it to make a type specimen book. It has survived not only five centuries, but also the leap into electronic typesetting, remaining essentially unchanged. It was popularised in the 1960s with the release of Letraset sheets containing Lorem Ipsum passages.</p>
<div class="btn" style="left:518px;top:948px;width:166px;height:52px;line-height:52px">Read More</div>

<!-- testimonial -->
<div class="abs testimonial" role="img" aria-label="Photograph of a pine forest under a cloudy sky"></div>
<div class="abs testimonial" style="background:none"><div class="abs bar"></div></div>
<h2 class="title light" style="top:1100px">What our <span>customers</span> are saying !</h2>
<p class="abs quote">" Lorem ipsum is simply dummy text of the printing and typesetting industry. "</p>
<p class="abs author">- Paul Wendell</p>
<div class="arrow" style="left:536px;top:1452px"><svg width="14" height="12"><path d="M7 1L2 6l5 5M12 1L7 6l5 5" stroke="#fff" fill="none" stroke-width="1.6"/></svg></div>
<div class="arrow" style="left:628px;top:1452px"><svg width="10" height="12"><path d="M2 1l5 5-5 5" stroke="#fff" fill="none" stroke-width="1.6"/></svg></div>

<!-- provide -->
<h2 class="title" style="top:1622px">What <span>Cedar Ridge</span> provide</h2>
<p class="script" style="top:1688px">Lorem ipsum is a dummy text</p>
<div class="photo" style="left:334px;top:1766px;width:526px;height:271px;background:
  radial-gradient(ellipse 250px 30px at 263px 250px,rgba(110,140,80,.9),rgba(110,140,80,0)),
  radial-gradient(ellipse 230px 110px at 263px 150px,rgba(196,178,146,.95),rgba(196,178,146,0)),
  radial-gradient(ellipse 200px 70px at 263px 70px,rgba(120,128,140,.85),rgba(120,128,140,0)),
  #fff" role="img" aria-label="Illustration of a two-storey suburban house with a garage"></div>
<div class="arrow grey" style="left:164px;top:1888px"><svg width="14" height="12"><path d="M7 1L2 6l5 5M12 1L7 6l5 5" stroke="#fff" fill="none" stroke-width="1.6"/></svg></div>
<div class="arrow grey" style="left:1000px;top:1888px;background:#888"><svg width="10" height="12"><path d="M2 1l5 5-5 5" stroke="#fff" fill="none" stroke-width="1.6"/></svg></div>

<!-- what's new -->
<div class="abs whatsnew" role="img" aria-label="Photograph of a warm wooden kitchen interior"></div>
<div class="abs whatsnew" style="background:none"><div class="abs shade"></div></div>
<h2 class="title light" style="top:2166px">What's <span>New</span></h2>
<div class="photo" style="left:216px;top:2266px;width:261px;height:249px;background:
  radial-gradient(ellipse 90px 80px at 110px 110px,rgba(196,90,70,.9),rgba(196,90,70,0)),
  radial-gradient(ellipse 80px 70px at 180px 170px,rgba(220,170,120,.9),rgba(220,170,120,0)),
  rgba(240,228,216,.0)" role="img" aria-label="Illustrated cutaway floor plan of a home"></div>
<div class="abs new-text">
  <p>Cedar Ridge Estates at Alder Point is quickly becoming Brookhaven' finest custom home community. In spring 2009, 9 of 49 custom homesites will be offering to the public. These lots are impressive with over 90 to 120 feet wide and are ranging from one-quarter to over half an acre in size.</p>
  <p style="margin-top:22px">In order to take advantage of the Pre-Development price, call now to place a fully refundable deposit for a reservation of these home sites.</p>
</div>
<div class="btn" style="left:516px;top:2533px;width:168px;height:52px;line-height:52px">Book Now !</div>
<p class="abs hurry">Hurry only <span>three</span> custom lots are available!</p>

<!-- recent work -->
<h2 class="title" style="top:2748px">Our recent <span>work</span></h2>
<p class="script" style="top:2811px">Lorem ipsum is a dummy text</p>
<div class="abs filters"><span class="on">All</span><span>Luxury Homes</span><span>Luxury Homesites</span><span>Community</span></div>
<div class="photo" style="left:80px;top:2928px;width:251px;height:175px;background:radial-gradient(ellipse 100px 60px at 125px 80px,#e6ddcc,rgba(230,221,204,0)),linear-gradient(180deg,#9ab0c8,#b8ab98 55%,#6c7a50)" role="img" aria-label="Photograph of a white two-storey home"></div>
<div class="abs" style="left:80px;top:2928px;width:251px;height:175px;background:rgba(0,0,0,.25)"></div>
<p class="abs" style="left:80px;top:3060px;width:251px;text-align:center;color:#fff;font-size:15px">Lorem ipsum text</p>
<div class="photo" style="left:341px;top:2928px;width:251px;height:175px;background:radial-gradient(ellipse 100px 50px at 125px 95px,#e4e0d8,rgba(228,224,216,0)),linear-gradient(180deg,#6f9ed6,#c8c4b8 55%,#5b7d3a)" role="img" aria-label="Photograph of a stately house with a green lawn"></div>
<div class="photo" style="left:605px;top:2928px;width:251px;height:175px;background:radial-gradient(ellipse 80px 40px at 125px 105px,#e2a050,rgba(226,160,80,0)),linear-gradient(180deg,#3c5e8c,#4a4a44 55%,#3e5a30)" role="img" aria-label="Photograph of a lit modern home among trees at dusk"></div>
<div class="photo" style="left:869px;top:2928px;width:251px;height:175px;background:linear-gradient(180deg,#cfe3f2,#8bb26a 45%,#c8b8a0 62%,#3ea6c2)" role="img" aria-label="Photograph of a resort pool lined with palm trees"></div>
<div class="photo" style="left:80px;top:3119px;width:251px;height:179px;background:radial-gradient(ellipse 110px 60px at 125px 90px,#eee6d6,rgba(238,230,214,0)),linear-gradient(180deg,#aac0d4,#d8ccb8 55%,#8a8a6a)" role="img" aria-label="Photograph of a white villa with columns"></div>
<div class="photo" style="left:341px;top:3119px;width:251px;height:179px;background:radial-gradient(ellipse 100px 50px at 125px 95px,#e4e0d8,rgba(228,224,216,0)),linear-gradient(180deg,#6f9ed6,#c8c4b8 55%,#5b7d3a)" role="img" aria-label="Photograph of a stately house with a green lawn"></div>
<div class="photo" style="left:605px;top:3119px;width:251px;height:179px;background:radial-gradient(ellipse 80px 40px at 125px 105px,#e2a050,rgba(226,160,80,0)),linear-gradient(180deg,#3c5e8c,#4a4a44 55%,#3e5a30)" role="img" aria-label="Photograph of a lit modern home among trees at dusk"></div>
<div class="photo" style="left:869px;top:3119px;width:251px;height:179px;background:linear-gradient(180deg,#cfe3f2,#8bb26a 45%,#c8b8a0 62%,#3ea6c2)" role="img" aria-label="Photograph of a resort pool lined with palm trees"></div>

<!-- team -->
<div class="abs team" role="img" aria-label="Photograph of colleagues in an office meeting"></div>
<div class="abs team" style="background:none"><div class="abs shade"></div></div>
<h2 class="title light" style="top:3394px">Our <span>Team</span></h2>
<div class="portrait" style="left:80px;background:radial-gradient(ellipse 90px 120px at 125px 150px,#c48a5a,rgba(196,138,90,0)),linear-gradient(180deg,#efe2cc,#d8b98e)" role="img" aria-label="Portrait photo of the administrator"></div>
<div class="portrait" style="left:344px;background:radial-gradient(ellipse 90px 120px at 125px 170px,#3c3c40,rgba(60,60,64,0)),linear-gradient(180deg,#f6f6f6,#e2e4e8)" role="img" aria-label="Portrait photo of the architect"></div>
<div class="portrait" style="left:607px;background:radial-gradient(ellipse 90px 120px at 125px 170px,#7f9cc2,rgba(127,156,194,0)),linear-gradient(180deg,#e8edf2,#c6d2de)" role="img" aria-label="Portrait photo of the head builder"></div>
<div class="portrait" style="left:871px;background:radial-gradient(ellipse 90px 120px at 125px 150px,#5a3e30,rgba(90,62,48,0)),linear-gradient(180deg,#f0efed,#d8d0c8)" role="img" aria-label="Portrait photo of the marketing head"></div>
<div class="member" style="left:80px"><div class="n">Lena Marlow</div><div class="r">Administrator</div></div>
<div class="member" style="left:344px"><div class="n">Owen Pritchard</div><div class="r">Architecture</div></div>
<div class="member" style="left:607px"><div class="n">Reid Callan</div><div class="r">Head Builder</div></div>
<div class="member" style="left:871px"><div class="n">Nora Fielding</div><div class="r">Marketing Head</div></div>

<!-- form -->
<h2 class="title" style="top:3976px">There's no better <span>time</span> than now</h2>
<p class="script" style="top:4040px">Get in touch, let's work together</p>
<div class="field focus" style="left:89px;top:4138px;width:500px;height:51px">Name</div>
<div class="field" style="left:89px;top:4201px;width:500px;height:51px">E-Mail</div>
<div class="field" style="left:89px;top:4265px;width:500px;height:51px">Phone</div>
<div class="field" style="left:611px;top:4138px;width:503px;height:178px">Message</div>
<div class="btn" style="left:516px;top:4335px;width:168px;height:51px;line-height:51px;background:#555;color:#fff">Book Now !</div>

<!-- contact -->
<div class="abs contact-band"></div>
<h2 class="title light" style="top:4464px">Contact <span>Us</span></h2>
<div class="abs socials"><i></i><i></i><i></i><i></i><i></i><i></i></div>
<div class="abs contact-lines">555.014.2290 | <a>hello@cedarridgehomes.com</a><br>4120 W. Orchard Lane, Brookhaven, CA 90000</div>
<div class="abs mini-mark"></div>
<div class="abs bottom-bar">© 2015 <span>CEDAR RIDGE</span>. All Rights Reserved.</div>

</body>
</html>
```